Create a Shopify weblayout for Haverlow Fashion Boutique

I would like a new website layout for my online fashion boutique www.haverlow-shop.example. My new online boutique is inspired by the 2 English writers of the 19th century. These books come from old English literature. Haverlow is a fictitious place withing these inspiring love stories. My boutique idea is inspired by old English landscape, unprecedented magic and influenced by bonds between improbable characters. My boutique is for woman initially, but I would like to add male products sometime in the future, hence the logo should be gender neutral.

I have started with a logo which I deciding upon these days. However, the professional website layout that I am looking for would be inspired by a creative visual from the above descriptions.

I do like white/black color scheme, but I would also like the layout to incorporate an additional color plus an additional design element. I was thinking of floral inspirations, like roses or green wine leaves, perhaps. I would like something with a mix of modern, magic, and eclectic. Thank you all in advance for your igniting ideas.

Project Deadline Extended Reason: Project extended due to holiday season. We are working on submitting feedback regarding our desired layout. Added Thursday, November 24, 2016

Target Market(s)

Online boutique for women and man clothing.

Industry/Entity Type

Fashion

Coding

Coded - Design and coding required

Number of Pages Required

4 page

Font styles to use
Other font styles liked:
• readable, but elegant and artsy

Requirements
Must have
• Elegant, artsy and legible. Embrace the logo (vector files will be uploaded shortly)
• Files must support use with Shopify. More boutique style less commercial. Simple details are nice. I like the efficiency of the commercial sites. Must have a mobile version. EXAMPLE: http://www.mabelsonwestcedar.example/ THIS IS A BEAUTIFUL SITE. in place of the yellow line it would be nice to have a vine maybe?
• Although i am stern on this, i don't mean this with any disrespect ever but please, don't call me or email me on my personal email. If we need to connect, we can do so after i pick a design. Thank you.
Nice to have
• It would be nice if the tree of the logo would be incorporate somewhere in the website. We are very much interested in little details. Please inspire us.

```html
<!DOCTYPE html>
<html lang="en">
<head>
<meta charset="utf-8">
<title>Haverlow Fashion Boutique</title>
<link rel="stylesheet" href="https://fonts.googleapis.com/css2?family=Playfair+Display:wght@400&family=Poppins:wght@400;500&display=swap">
<style>
  :root {
    --navy: #1f2d3d;
    --navy-deep: #1a2633;
    --navy-card: #223244;
    --paper: #ffffff;
    --card-photo: #eeeef2;
    --ink: #2a2f38;
    --muted: #7b8490;
    --line: #c9d0d8;
    --star: #e8a33a;
    --tag: #1f2d3d;
  }
  * { margin: 0; padding: 0; box-sizing: border-box; }
  html, body { width: 798px; height: 1200px; overflow: hidden; }
  body {
    position: relative;
    background: var(--navy);
    font-family: 'Poppins', sans-serif;
    color: var(--paper);
  }
  .abs { position: absolute; }
  .serif { font-family: 'Playfair Display', serif; }

  /* header */
  .nav a { position: absolute; top: 20px; font-size: 10px; color: var(--paper); text-decoration: none; }
  .nav a.active { color: #9aa4ae; }
  .brand { left: 339px; top: 18px; width: 120px; text-align: center; font-family: 'Playfair Display', serif; font-size: 16px; letter-spacing: 1px; color: var(--paper); }
  .cart { left: 718px; top: 20px; }

  /* hero */
  .hero { left: 59px; top: 50px; width: 680px; height: 320px;
    background: linear-gradient(100deg, #2b3440 0%, #6b7684 35%, #c8cdd2 55%, #8ab8c4 80%, #3a3f45 100%); }
  .hero-card { left: 42px; top: 250px; width: 159px; height: 120px; background: var(--paper); color: var(--ink); padding: 20px 18px 0 18px; }
  .hero-card h2 { font-family: 'Playfair Display', serif; font-weight: 400; font-size: 12.5px; margin-bottom: 9px; }
  .hero-card p { font-size: 7.5px; line-height: 13px; color: #6b7380; }
  .hero-card .shop { position: absolute; right: 24px; bottom: 15px; font-size: 6.5px; color: #555; }

  .section-title { width: 798px; text-align: center; font-family: 'Playfair Display', serif; font-size: 15px; left: 0; }

  /* products */
  .product { top: 444px; width: 166px; height: 202px; background: var(--paper); color: var(--ink); }
  .product .photo { position: absolute; left: 0; top: 0; width: 166px; height: 160px; background: var(--card-photo); }
  .product .price { position: absolute; left: 10px; top: 166px; font-size: 8.5px; }
  .product .name { position: absolute; left: 10px; top: 179px; font-size: 8.5px; font-weight: 500; color: #444; }
  .product .count { position: absolute; right: 10px; top: 168px; font-size: 6.5px; }
  .product .stars { position: absolute; right: 9px; top: 180px; font-size: 7px; letter-spacing: 1px; color: var(--star); }
  .product .stars b { color: #555; font-weight: 400; }

  .btn { border: 1px solid var(--paper); font-size: 8.5px; text-align: center; line-height: 24px; height: 26px; color: var(--paper); }

  /* blogs */
  .blog { top: 761px; width: 211px; height: 218px; background: var(--paper); color: var(--ink); }
  .blog.hover { background: var(--navy-card); color: var(--paper); }
  .blog .photo { position: absolute; left: 0; top: 0; width: 211px; height: 113px; }
  .blog .tag { position: absolute; left: 18px; top: 127px; background: var(--tag); color: var(--paper); font-size: 6px; font-weight: 500; padding: 2px 5px; }
  .blog h3 { position: absolute; left: 18px; top: 146px; font-family: 'Playfair Display', serif; font-weight: 400; font-size: 11px; }
  .blog .meta { position: absolute; left: 18px; top: 168px; font-size: 6.5px; color: #666; }
  .blog.hover .meta { color: #b8c0c8; }
  .blog .rule { position: absolute; left: 18px; top: 185px; width: 16px; height: 1px; background: var(--line); }
  .blog .read { position: absolute; left: 17px; top: 196px; font-size: 6.5px; }

  /* footer */
  .footer { left: 0; top: 1042px; width: 798px; height: 128px; background: var(--navy-deep); }
  .foot-col { top: 1072px; }
  .foot-col h4 { font-family: 'Playfair Display', serif; font-weight: 400; font-size: 11.5px; }
  .foot-col .under { width: 20px; height: 1px; background: var(--paper); margin: 4px 0 10px; }
  .foot-col li { list-style: none; font-size: 8px; line-height: 15px; }
  .subscribe-field { left: 59px; top: 1104px; width: 137px; height: 24px; background: #223140; font-size: 7px; color: #aab2bb; padding: 8px 10px; }
  .subscribe-go { left: 196px; top: 1104px; width: 26px; height: 24px; background: #15202c; }
  .bottom { left: 0; top: 1170px; width: 798px; height: 30px; background: var(--paper); color: var(--ink); font-size: 8px; }
  .pay { top: 9px; width: 22px; height: 13px; border-radius: 2px; }
</style>
</head>
<body>

<nav class="nav">
  <a class="active" style="left:64px">Home</a>
  <a style="left:117px">The Team</a>
  <a style="left:187px">Designer Lines</a>
  <a style="left:537px">Contact us</a>
  <a style="left:612px">Login</a>
  <a style="left:662px">Register</a>
</nav>
<div class="abs brand">Haverlow</div>
<svg class="abs cart" width="14" height="11" viewBox="0 0 14 11" fill="none" stroke="#fff" stroke-width="1">
  <path d="M0.5 1h2l1.5 6h6l1.5-4.5H3.5"/><circle cx="5" cy="9.3" r="0.9"/><circle cx="9.5" cy="9.3" r="0.9"/>
</svg>

<div class="abs hero" role="img" aria-label="Photo of a smiling couple browsing clothes on a shop rail"></div>
<div class="abs hero-card">
  <h2>Haverlow Fashion</h2>
  <p>Lorem aenean vulputate eleifend tellus aenean leo ligula porttitor eu dolor sit.</p>
  <span class="shop">SHOP NOW &rarr;</span>
</div>

<div class="abs section-title" style="top:410px">Haverlow’s Collection</div>

<div class="abs product" style="left:61px">
  <div class="photo" role="img" aria-label="Purple fedora hat" style="background:radial-gradient(ellipse 40% 22% at 50% 50%, #6a55d0 0%, #8c7ad8 60%, var(--card-photo) 100%)"></div>
  <span class="price">$16.90</span><span class="name">Product name here</span>
  <span class="count">24</span><span class="stars"><b>★</b>★★★★</span>
</div>
<div class="abs product" style="left:230px">
  <div class="photo" role="img" aria-label="Blue denim shirt" style="background:radial-gradient(ellipse 35% 38% at 50% 50%, #2c4c8a 0%, #4f6ea8 60%, var(--card-photo) 100%)"></div>
  <span class="price">$25.45</span><span class="name">Product name here</span>
  <span class="count">24</span><span class="stars"><b>★</b>★★★★</span>
</div>
<div class="abs product" style="left:400px">
  <div class="photo" role="img" aria-label="Grey canvas sneaker" style="background:radial-gradient(ellipse 45% 18% at 50% 55%, #8a8a86 0%, #c4c4c0 60%, var(--card-photo) 100%)"></div>
  <span class="price">$12.00</span><span class="name">Product name here</span>
  <span class="count">24</span><span class="stars"><b>★</b>★★★★</span>
</div>
<div class="abs product" style="left:570px">
  <div class="photo" role="img" aria-label="Pair of white loafers" style="background:radial-gradient(ellipse 30% 35% at 50% 45%, #ffffff 0%, #dcdde2 60%, var(--card-photo) 100%)"></div>
  <span class="price">$54.75</span><span class="name">Product name here</span>
  <span class="count">24</span><span class="stars"><b>★</b>★★★★</span>
</div>

<div class="abs btn" style="left:356px; top:664px; width:86px">View full boutique</div>

<div class="abs section-title" style="top:727px">Blogs</div>

<div class="abs blog" style="left:59px">
  <div class="photo" role="img" aria-label="Two women with colourful shopping bags" style="background:linear-gradient(90deg,#c9a24a,#e6d36a 40%,#8fd0de 70%,#e39a4a)"></div>
  <span class="tag">FASHION</span>
  <h3>Lorem ipsum dolor dummy.</h3>
  <span class="meta">&#9679; By: admin &nbsp;&nbsp; &#9633; Posted on: 20.July.2016</span>
  <span class="rule"></span>
  <span class="read">READ BLOG &nbsp;&rarr;</span>
</div>
<div class="abs blog hover" style="left:294px">
  <div class="photo" role="img" aria-label="Woman checking a price tag in a clothing store" style="background:linear-gradient(90deg,#6a4a38,#b09080 35%,#d8d4cf 60%,#5a6a82)"></div>
  <span class="tag" style="background:#16212d">WOMEN</span>
  <h3>Lorem ipsum dolor dummy.</h3>
  <span class="meta">&#9679; By: admin &nbsp;&nbsp; &#9633; Posted on: 20.July.2016</span>
  <span class="read">READ BLOG &nbsp;&rarr;</span>
</div>
<div class="abs blog" style="left:528px">
  <div class="photo" role="img" aria-label="Couple walking through a shopping mall with bags" style="background:linear-gradient(90deg,#5d88b0,#dfe4e8 40%,#f2f2f2 60%,#4f7db6)"></div>
  <span class="tag">TRENDS</span>
  <h3>Lorem ipsum dolor dummy.</h3>
  <span class="meta">&#9679; By: admin &nbsp;&nbsp; &#9633; Posted on: 20.July.2016</span>
  <span class="rule"></span>
  <span class="read">READ BLOG &nbsp;&rarr;</span>
</div>

<div class="abs btn" style="left:368px; top:998px; width:63px">More Blogs</div>

<footer class="abs footer"></footer>
<div class="abs foot-col" style="left:59px"><h4>Subscribe</h4><div class="under"></div></div>
<div class="abs subscribe-field">Email address</div>
<div class="abs subscribe-go"><svg width="26" height="24" viewBox="0 0 26 24" fill="none" stroke="#fff" stroke-width="1"><path d="M9 12h8M14 9l3 3-3 3"/></svg></div>
<div class="abs foot-col" style="left:288px"><h4>Navigation</h4><div class="under"></div><ul><li>Home</li><li>Search</li><li>About us</li></ul></div>
<div class="abs foot-col" style="left:430px"><h4>Shop by collection</h4><div class="under"></div><ul><li>Business / Formal</li><li>Casual</li><li>Party</li></ul></div>
<div class="abs foot-col" style="left:584px"><h4>Shop by category</h4><div class="under"></div><ul><li>Men</li><li>Women</li><li>All</li></ul></div>

<div class="abs bottom">
  <span class="abs" style="left:60px; top:9px">© Haverlow</span>
  <span class="abs pay" style="left:642px; background:#ffffff; border:1px solid #d7dbe0"></span>
  <span class="abs pay" style="left:668px; background:#e05a2a"></span>
  <span class="abs pay" style="left:692px; background:#2a2a2a"></span>
  <span class="abs pay" style="left:716px; background:#f4eed8"></span>
</div>

</body>
</html>
```